Business Coach needs an elegant business card design

I need a business card design based around my logo for color and to look like a millionaire dollar coach. Incorporate the color of my logo with something creative and attractive that stands out. I am focused on high end companies and the card must look and feel that way.

Target Market(s)

High End Companies and Business Owners - Training People to become millionaires

Industry/Entity Type

Business

Requirements
Must have
• Front -
Logo (attached file) - Website (marlowkeeve.com) - Name (Marlow Keeve) Phone (555.201.7746) - Email (marlow@marlowkeeve.com) (My Title - Success Coach)
Back -
Slogan - Purpose (find it) . Growth (build it) . Legacy (own it)
Website - Learn More @ marlowkeeve.com

Creative High End Look!
Nice to have
Should not have
• Cheap standard look
nothing traditional

```html
<!DOCTYPE html>
<html lang="en">
<head>
<meta charset="utf-8">
<title>Marlow Keeve Coaching — Business Card</title>
<link href="https://fonts.googleapis.com/css2?family=Cinzel:wght@500&family=Cormorant+Garamond:wght@500&family=Questrial&display=swap" rel="stylesheet">
<style>
  :root {
    --page: #f4f4f4;
    --ink-black: #050505;
    --ink-navy: #213a63;
    --stone: #8a8480;
    --stone-navy: #6c7a92;
    --paper: #ffffff;
    --muted: #c9cfdb;
    --soft: #dcdcdc;
  }
  * { margin: 0; padding: 0; box-sizing: border-box; }
  html, body { width: 1200px; height: 873px; overflow: hidden; background: var(--page); }
  .sheet {
    width: 1200px; height: 873px;
    display: flex; align-items: center; justify-content: center; gap: 60px;
  }
  .card {
    position: relative; width: 520px; height: 297px; overflow: hidden;
    box-shadow: 0 10px 28px rgba(0,0,0,.18);
    color: var(--paper);
  }
  .card--front { background: var(--ink-black); }
  .card--back { background: var(--ink-navy); }

  .emblem-circle { position: absolute; border-radius: 50%; }
  .card--front .emblem-circle {
    width: 300px; height: 300px; left: -120px; top: -25px; background: var(--stone);
    box-shadow: 0 0 0 6px var(--ink-black), 0 0 0 16px var(--stone);
  }
  .card--back .emblem-circle {
    width: 220px; height: 220px; left: 150px; bottom: -120px;
    background: var(--stone-navy); opacity: .55;
    box-shadow: 0 0 0 5px var(--ink-navy), 0 0 0 13px var(--stone-navy);
  }

  .brand { position: absolute; display: flex; align-items: center; gap: 10px; }
  .brand__dot {
    width: 30px; height: 30px; border-radius: 50%;
    border: 2px solid var(--paper);
  }
  .brand__name {
    font-family: "Cinzel", serif; font-weight: 500; line-height: 1.05;
    letter-spacing: .04em; color: var(--paper); text-transform: uppercase;
  }
  .brand__name span { display: block; font-size: .55em; letter-spacing: .3em; }
  .card--front .brand { right: 24px; top: 22px; }
  .card--front .brand__name { font-size: 16px; }
  .card--back .brand { left: 120px; top: 52px; }
  .card--back .brand__dot { width: 44px; height: 44px; border-width: 3px; }
  .card--back .brand__name { font-size: 28px; }

  .identity { position: absolute; left: 240px; top: 108px; }
  .identity__name {
    font-family: "Cinzel", serif; font-weight: 500; font-size: 24px; letter-spacing: .03em;
  }
  .identity__title {
    font-family: "Cormorant Garamond", serif; font-weight: 500; font-size: 14px;
    margin-top: 0; color: var(--soft);
  }
  .contacts { list-style: none; margin-top: 16px; font-family: "Questrial", sans-serif; font-size: 17px; }
  .contacts li { display: flex; align-items: center; gap: 10px; margin-bottom: 5px; white-space: nowrap; }
  .contacts svg { width: 13px; height: 13px; flex: none; }

  .slogan {
    position: absolute; left: 40px; top: 136px; width: 440px;
    font-family: "Questrial", sans-serif; font-size: 13px; line-height: 1.6;
    color: var(--muted); text-align: center;
  }
</style>
</head>
<body>
<main class="sheet">
  <section class="card card--front" aria-label="Business card front">
    <div class="emblem-circle"></div>
    <div class="brand">
      <div class="brand__dot"></div>
      <div class="brand__name">Marlow Keeve<span>Coaching</span></div>
    </div>
    <div class="identity">
      <h1 class="identity__name">MARLOW KEEVE</h1>
      <p class="identity__title">Success Coach</p>
      <ul class="contacts">
        <li>
          <svg viewBox="0 0 16 16" aria-hidden="true"><circle cx="8" cy="8" r="7" fill="none" stroke="#fff" stroke-width="1.4"/><path d="M5.5 4.5l1.5 0 .6 2-1 .8a5 5 0 0 0 2.2 2.2l.8-1 2 .6v1.5c-3.5.4-6.5-2.6-6.1-6.1z" fill="#fff"/></svg>
          555.201.7746
        </li>
        <li>
          <svg viewBox="0 0 16 16" aria-hidden="true"><rect x="1.5" y="3.5" width="13" height="9" fill="none" stroke="#fff" stroke-width="1.4"/><path d="M1.5 3.5l6.5 5 6.5-5" fill="none" stroke="#fff" stroke-width="1.4"/></svg>
          marlow@marlowkeeve.com
        </li>
        <li>
          <svg viewBox="0 0 16 16" aria-hidden="true"><circle cx="8" cy="8" r="6.5" fill="none" stroke="#fff" stroke-width="1.3"/><ellipse cx="8" cy="8" rx="2.8" ry="6.5" fill="none" stroke="#fff" stroke-width="1.1"/><path d="M1.5 8h13" stroke="#fff" stroke-width="1.1"/></svg>
          www.marlowkeeve.com
        </li>
      </ul>
    </div>
  </section>

  <section class="card card--back" aria-label="Business card back">
    <div class="emblem-circle"></div>
    <div class="brand">
      <div class="brand__dot"></div>
      <div class="brand__name">Marlow Keeve<span>Coaching</span></div>
    </div>
    <p class="slogan">Purpose (find it) . Growth (build it) . Legacy (own it)<br>Learn More @marlowkeeve.com</p>
  </section>
</main>
</body>
</html>
```